Dovantix - "Where Pest Control is Free for Life..." Please see pitch deck...

Project goal, that this is a reusable template, not a one-off card
Brand and design direction, follow the logo, use the brand palette (with a color swatch table), typography and layout guidance
The John Doe placeholder content as a clean field-by-field table (name, title, company, address, office, cell, fax, email, dovantix.com)
Print specs, 3.5 × 2 in trim, 0.125 in bleed, 300 DPI, CMYK, crop marks
Deliverables, layered editable PSD (your primary ask) plus vector .AI/.EPS and a press-ready PDF/X-1a, with fonts packaged
What you'll provide (logo, colors, fonts)
Process and sign-off, concept first, then full file package on approval.
Populate every field with this John Doe placeholder data so we can see the layout fully built out. We will replace it per person.
Name John Doe
Title Title / Position
Company Dovantix
Address 123 Main Street, Suite 100, Tallahassee, FL 32301
Office (850) 555-0100
Cell (850) 555-0123
Fax (850) 555-0199
Email johndoe@dovantix.com
Website dovantix.com

We need the working, editable source files so we can update them ourselves, plus a ready-to-print export:
1. Photoshop (.PSD) — fully layered and editable, with each contact field on its own labeled text layer. This is the primary requested format.
2. Vector source — the press-standard editable format, Adobe Illustrator (.AI) and/or .EPS, since vector is preferred for crisp text and logos at print.
3. Print-ready PDF — press-quality (PDF/X-1a), CMYK, with bleed and crop marks, both sides.
4. Packaged fonts and links — include or list all fonts used, and package any linked assets so the files open correctly on our end.

Why both PSD and vector
The PSD covers our request directly and is easy for us to edit. Vector (.AI/.EPS) is what most commercial printers actually prefer for type and logos because it stays razor-sharp at any size. Providing both keeps us flexible no matter which printer we use. Have fun and keep it modern and cool the designer of the logo did a great job, see what you can do.

```html
<!DOCTYPE html>
<html lang="en">
<head>
<meta charset="utf-8">
<title>Dovantix Business Card</title>
<link rel="stylesheet" href="https://fonts.googleapis.com/css2?family=Lato:wght@400;700;900&family=Montserrat:wght@700&display=swap">
<style>
  :root {
    --stage: #1c1c1c;
    --card: #000000;
    --teal: #0bb3c6;
    --white: #ffffff;
  }
  * { margin: 0; padding: 0; box-sizing: border-box; }
  html, body {
    width: 1200px;
    height: 1059px;
    overflow: hidden;
    background: var(--stage);
  }
  .canvas {
    position: relative;
    width: 1200px;
    height: 1059px;
  }
  .card {
    position: absolute;
    left: 254px;
    width: 694px;
    height: 396px;
    background: var(--card);
    border-radius: 26px;
    box-shadow: 0 10px 28px rgba(0,0,0,0.6);
  }
  .card--front { top: 85px; }
  .card--back { top: 548px; }

  .brand {
    position: absolute;
    left: 0;
    width: 100%;
    display: flex;
    justify-content: center;
    align-items: center;
    gap: 14px;
    font-family: "Lato", sans-serif;
    font-weight: 900;
    color: var(--white);
    letter-spacing: -1px;
    line-height: 1;
  }
  .brand__mark {
    width: 22px;
    height: 22px;
    background: var(--teal);
  }
  .card--front .brand { top: 55px; font-size: 84px; }
  .card--back .brand { top: 150px; font-size: 92px; }
  .card--back .brand__mark { width: 24px; height: 24px; }

  .identity {
    position: absolute;
    right: calc(694px - 305px);
    top: 193px;
    text-align: right;
    font-family: "Lato", sans-serif;
    color: var(--white);
  }
  .identity__name {
    font-family: "Montserrat", sans-serif;
    font-weight: 700;
    font-size: 26px;
    color: var(--teal);
    letter-spacing: 0.5px;
    line-height: 1.1;
  }
  .identity__title {
    font-size: 19px;
    font-weight: 400;
    margin-top: 2px;
    letter-spacing: 0.5px;
  }
  .identity__address {
    font-style: normal;
    font-size: 19px;
    line-height: 23px;
    margin-top: 4px;
  }

  .divider {
    position: absolute;
    left: 333px;
    top: 188px;
    width: 2px;
    height: 131px;
    background: var(--teal);
  }

  .contacts {
    position: absolute;
    left: 352px;
    top: 183px;
    list-style: none;
    font-family: "Lato", sans-serif;
    font-size: 19px;
    color: var(--white);
  }
  .contacts__item {
    display: flex;
    align-items: center;
    height: 28px;
    margin-bottom: 1px;
  }
  .contacts__icon {
    width: 20px;
    height: 20px;
    margin-right: 10px;
    fill: var(--teal);
    flex: none;
  }
</style>
</head>
<body>
<main class="canvas">

  <section class="card card--front" aria-label="Card front">
    <div class="brand">
      <span class="brand__name">Dovantix</span>
      <span class="brand__mark"></span>
    </div>

    <div class="identity">
      <p class="identity__name">JOHN DOE</p>
      <p class="identity__title">Owner</p>
      <address class="identity__address">
        123 Main Street,<br>
        Suite 100, Tallahassee,<br>
        FL 32301
      </address>
    </div>

    <div class="divider"></div>

    <ul class="contacts">
      <li class="contacts__item">
        <svg class="contacts__icon" viewBox="0 0 20 20"><path d="M2 7c0-2 3-3 8-3s8 1 8 3v2h-4V7H6v2H2z"/><path d="M5 10h10l2 7H3z"/></svg>
        <span>(850) 555-0100</span>
      </li>
      <li class="contacts__item">
        <svg class="contacts__icon" viewBox="0 0 20 20"><path d="M6 1h8a1 1 0 0 1 1 1v16a1 1 0 0 1-1 1H6a1 1 0 0 1-1-1V2a1 1 0 0 1 1-1zm1 3v11h6V4z"/><circle cx="10" cy="17" r="1" fill="#000"/></svg>
        <span>(850) 555-0123</span>
      </li>
      <li class="contacts__item">
        <svg class="contacts__icon" viewBox="0 0 20 20"><rect x="1" y="6" width="4" height="13"/><path d="M6 8h13v11H6z"/><rect x="8" y="2" width="8" height="5"/></svg>
        <span>(850) 555-0199</span>
      </li>
      <li class="contacts__item">
        <svg class="contacts__icon" viewBox="0 0 20 20"><path d="M1 4h18v12H1z"/><path d="M1 4l9 7 9-7" fill="none" stroke="#000" stroke-width="1.6"/></svg>
        <span>johndoe@dovantix.com</span>
      </li>
      <li class="contacts__item">
        <svg class="contacts__icon" viewBox="0 0 20 20"><circle cx="10" cy="10" r="8.5" fill="none" stroke="var(--teal)" stroke-width="2"/><path d="M6 5c2 0 3 2 2 4s1 4-1 6c-2-2-3-6-1-10zM12 4c2 1 4 3 4 6-2 0-3-1-3-3z"/></svg>
        <span>www.dovantix.com</span>
      </li>
    </ul>
  </section>

  <section class="card card--back" aria-label="Card back">
    <div class="brand">
      <span class="brand__name">Dovantix</span>
      <span class="brand__mark"></span>
    </div>
  </section>

</main>
</body>
</html>
```